Plant Grower/Nursery needs a fun, professional and fresh 1/2 page print ad for a high profile gar...

We need a print ad for a garden tour geared towards plant enthusiasts that support California Native, natural and sustainable plants. A good percentage of our target market want a conservation and earth friendly approach to gardens/landscaping. We want to target this market, as well as, people who are looking for a pretty/colorful landscape that require little water/maintenance. **PLEASE LET US KNOW IF YOU HAVE QUESTIONS OR NEED MORE INFORMATION. WE ALSO HAVE MANY MORE PICTURES IF THESE DON'T WORK FOR YOUR DESIGN. ***THE AD CAN HAVE AS FEW AS 1 PHOTO - WE ARE POSTING SEVERAL IN HOPES THAT YOU CAN FIND WHAT IS PERFECT FOR YOUR IDEA!!Thank you

Target Market(s)

Gardeners, Landscapers, Landscape Designers/Architects, Cities and Municipalities.

Industry/Entity Type

Agriculture

Font styles to use
Serif
Sans Serif

Colors

Requirements
Must have
• We believe in growing regionally appropriate plants for Southern California that beatify our natural and urban landscapes.
• For over 20 years, our owners and staff take pride in providing timely, expert, and honest service.
Nice to have
• At least 1 photo. Eye catchy with a modern earthy feel.
• Hundreds of species/hybrids in stock of California Natives, Succulents, Ornamental Grasses, Standard Stock Items and Unique Plants.

```html
<!DOCTYPE html>
<html lang="en">
<head>
<meta charset="utf-8">
<title>Canyon Bloom Growers – Gardening and Landscaping Tour</title>
<link href="https://fonts.googleapis.com/css2?family=Playfair+Display:ital,wght@0,700;1,700&family=Open+Sans:ital,wght@0,400;0,600;0,700;1,700&display=swap" rel="stylesheet">
<style>
  :root {
    --page-bg: #e9e9ea;
    --paper: #ffffff;
    --teal: #1d7f95;
    --teal-dark: #145e70;
    --leaf: #7cc142;
    --leaf-dark: #4f9a2a;
    --violet: #6a2c91;
    --violet-deep: #4b1c6b;
    --sun: #f3e43a;
    --body-ink: #3c3c3c;
  }
  * { box-sizing: border-box; margin: 0; padding: 0; }
  html, body { width: 880px; height: 1200px; overflow: hidden; }
  body {
    background: var(--page-bg);
    font-family: "Open Sans", Arial, sans-serif;
    position: relative;
  }
  .ad {
    position: absolute;
    left: 20px; top: 320px;
    width: 840px; height: 560px;
    background: var(--paper);
    overflow: hidden;
    box-shadow: 0 4px 18px rgba(0,0,0,.18);
  }
  .ad-shapes { position: absolute; inset: 0; }

  /* left column */
  .brand-block {
    position: absolute; left: 30px; top: 36px; width: 360px;
    display: flex; flex-direction: column; align-items: center;
  }
  .brand {
    display: flex; align-items: center; gap: 10px;
  }
  .brand-mark { width: 24px; height: 24px; border-radius: 50%; background: var(--violet); flex: none; }
  .brand-name {
    font-family: "Playfair Display", Georgia, serif;
    font-weight: 700; font-size: 22px; letter-spacing: 0.5px;
    color: var(--teal); text-transform: uppercase; white-space: nowrap;
  }
  .brand-tagline {
    margin-top: 4px;
    font-size: 11px; font-style: italic; color: var(--body-ink);
  }
  .copy { position: absolute; left: 40px; top: 120px; width: 340px; }
  .copy-lead {
    font-family: "Playfair Display", Georgia, serif;
    font-size: 18px; line-height: 1.35; color: var(--teal); font-weight: 700;
    margin-bottom: 16px;
  }
  .copy p { font-size: 13.5px; line-height: 1.5; color: var(--body-ink); margin-bottom: 12px; }
  .copy strong { color: var(--teal-dark); }

  .call {
    position: absolute; left: 40px; bottom: 22px;
    font-weight: 700; font-style: italic; font-size: 26px; color: var(--paper);
    white-space: nowrap;
  }

  /* right column */
  .tour-title {
    position: absolute; left: 460px; top: 28px; width: 360px;
    font-family: "Playfair Display", Georgia, serif;
    font-weight: 700; font-size: 38px; line-height: 1.1;
    color: var(--sun); text-align: center;
  }
  .tour-title .joiner { font-size: 22px; }
  .flower-photo {
    position: absolute; left: 428px; top: 168px; width: 412px; height: 338px;
    background:
      radial-gradient(ellipse at 30% 40%, #9b6fd0 0%, transparent 55%),
      radial-gradient(ellipse at 75% 65%, #7a4bb5 0%, transparent 60%),
      linear-gradient(180deg, #8f6bc4 0%, #6e4a9e 45%, #4f7a3a 100%);
  }
  .site {
    position: absolute; right: 26px; bottom: 18px;
    font-size: 19px; font-style: italic; font-weight: 600; color: var(--paper);
    white-space: nowrap;
  }
</style>
</head>
<body>
  <section class="ad">
    <svg class="ad-shapes" width="840" height="560" viewBox="0 0 840 560" aria-hidden="true">
      <path d="M420 0 H840 V180 H420 Z" fill="var(--leaf)"/>
      <path d="M400 0 C440 60 430 140 470 180 L420 180 L400 180 Z" fill="var(--violet)"/>
      <path d="M0 470 C140 440 300 500 420 490 L420 560 L0 560 Z" fill="var(--leaf)"/>
      <path d="M0 492 C150 468 300 520 420 512 L420 560 L0 560 Z" fill="var(--violet)"/>
      <path d="M420 500 H840 V560 H420 Z" fill="var(--violet)"/>
      <path d="M420 500 C560 486 700 510 840 494 L840 504 C700 520 560 498 420 510 Z" fill="var(--leaf)"/>
      <path d="M418 0 C458 160 398 360 430 560 L420 560 C388 360 448 160 408 0 Z" fill="var(--leaf-dark)"/>
    </svg>

    <div class="brand-block">
      <div class="brand">
        <span class="brand-mark"></span>
        <span class="brand-name">Canyon Bloom Growers</span>
      </div>
      <div class="brand-tagline">A family owned nursery company</div>
    </div>

    <div class="copy">
      <p class="copy-lead">We believe in growing regionally appropriate plants for Southern California that beautify our natural and urban landscapes.</p>
      <p><strong>For over 20 years,</strong> our owners and staff take pride in providing timely, expert, and honest service.</p>
      <p>Hundreds of species/hybrids in stock of California Natives, Succulents, Ornamental Grasses, Standard Stock Items and Unique Plants.</p>
    </div>

    <div class="call">Call Us : 555.014.2730</div>

    <h1 class="tour-title">Gardening <span class="joiner">and</span><br>Landscaping Tour</h1>
    <div class="flower-photo" role="img" aria-label="Photo of a field of purple native wildflowers in bloom"></div>
    <div class="site">canyonbloomgrowers.com</div>
  </section>
</body>
</html>
```